Electrical Business Card Design

New electrical business targeting my local area
Installations
Repairs
Switchboards
TV / Vistacast / Antennas
Telephone
Data Networks
Audio Visual
Licence # 518427K
ABN 58316927405
I would like some white background, black writing, red, blue & green can be used
Designer discretion to be used on layout, colour placement & any images
Reason: To give designers more time, I thought 5 days wasn't enough
Please don't just create generic business cards................include personal details e.g. business name, contact name, ph #, email. Also include the things I do, licence # & abn (refer to brief for all details)
Thanks
Reason: Would like more designs & have now committed my payment, thank you
Industry/Entity Type
Electrical
Contact Information for Business Card
Korvane Electrical Services,
Gareth Pelling,
0438 571 963,
korvaneelectrical@wexmail.net.au,
My suburb is Marbury
Look and feel

```html
<!DOCTYPE html>
<html lang="en">
<head>
<meta charset="utf-8">
<title>Korvane Electrical Services – Business Card</title>
<link rel="stylesheet" href="https://fonts.googleapis.com/css2?family=Source+Sans+3:wght@300;400&family=Quicksand:wght@400;600&display=swap">
<style>
  :root {
    --backdrop: #6f6b6b;
    --card-blue: #176db5;
    --card-white: #ffffff;
    --ink: #222222;
    --on-blue: #eef3fa;
    --on-blue-soft: #bcd3ee;
    --dot-red: #e2272e;
    --dot-green: #27a544;
    --dot-blue: #1aa3e0;
  }
  * { box-sizing: border-box; margin: 0; padding: 0; }
  html, body { width: 1200px; height: 750px; overflow: hidden; }
  body {
    background: var(--backdrop);
    position: relative;
    font-family: "Source Sans 3", "Helvetica Neue", Arial, sans-serif;
  }
  .card {
    position: absolute;
    top: 210px;
    width: 540px;
    height: 330px;
    overflow: hidden;
    box-shadow: 0 18px 40px rgba(0,0,0,.35);
  }
  /* Front */
  .card--front { left: 35px; background: var(--card-white); }
  .front__band {
    position: absolute; inset: 0 0 auto 0; height: 218px;
    background: var(--card-blue);
  }
  .business-name {
    position: absolute; left: 40px; top: 28px; width: 280px;
    color: var(--on-blue);
    font-weight: 300; font-size: 41px; line-height: 1.18;
    letter-spacing: 6px; text-align: center;
  }
  .business-name span { display: block; }
  .front__divider {
    position: absolute; left: 336px; top: 20px;
    width: 1px; height: 178px; background: var(--on-blue);
  }
  .contact-name {
    position: absolute; left: 362px; top: 58px;
    color: var(--on-blue); font-size: 23px; font-weight: 400; line-height: 1.15;
  }
  .contact-list {
    position: absolute; left: 26px; top: 236px; list-style: none;
    font-family: "Quicksand", "Century Gothic", sans-serif; color: var(--ink);
  }
  .contact-list li { display: flex; align-items: center; height: 24px; font-size: 17px; }
  .contact-list li.suburb { font-weight: 600; font-size: 16px; }
  .contact-list li.email { font-size: 13px; }
  .contact-list .dot { width: 10px; height: 10px; border-radius: 50%; margin-right: 6px; flex: none; }
  .dot--red { background: var(--dot-red); }
  .dot--green { background: var(--dot-green); }
  .dot--blue { background: var(--dot-blue); }
  .tagline {
    position: absolute; right: 28px; top: 240px;
    font-family: "Quicksand", "Century Gothic", sans-serif;
    font-size: 14px; color: var(--ink); letter-spacing: -.3px;
  }
  /* Back */
  .card--back { left: 625px; background: var(--card-blue); color: var(--on-blue); }
  .services__title {
    position: absolute; left: 150px; top: 38px;
    font-size: 25px; font-weight: 300; letter-spacing: 4px;
  }
  .services {
    position: absolute; top: 82px; list-style: none;
    font-size: 23px; font-weight: 300; letter-spacing: 2px; line-height: 32px;
  }
  .services--left { left: 28px; }
  .services--right { right: 22px; text-align: right; }
  .services li { display: flex; align-items: center; gap: 6px; }
  .services--right li { justify-content: flex-end; }
  .services .bullet { width: 8px; height: 8px; border-radius: 50%; background: var(--card-white); flex: none; }
  .reg {
    position: absolute; bottom: 22px;
    font-size: 13px; color: var(--on-blue-soft); letter-spacing: .5px;
  }
  .reg--licence { left: 26px; }
  .reg--abn { right: 26px; }
</style>
</head>
<body>
  <section class="card card--front" aria-label="Business card front">
    <div class="front__band"></div>
    <h1 class="business-name"><span>Korvane</span><span>Electrical</span><span>Services</span></h1>
    <div class="front__divider"></div>
    <p class="contact-name">Gareth<br>Pelling</p>
    <ul class="contact-list">
      <li class="suburb"><span class="dot dot--red"></span>Marbury</li>
      <li class="phone"><span class="dot dot--green"></span>0438 571 963</li>
      <li class="email"><span class="dot dot--blue"></span>korvane@wexmail.net.au</li>
    </ul>
    <p class="tagline">Reliable. Honest.</p>
  </section>

  <section class="card card--back" aria-label="Business card back">
    <h2 class="services__title">Things I do:</h2>
    <ul class="services services--left">
      <li><span class="bullet"></span>Installations</li>
      <li><span class="bullet"></span>TV/Vistacast/Antennas</li>
      <li><span class="bullet"></span>Repairs &amp; additions</li>
    </ul>
    <ul class="services services--right">
      <li>Phones<span class="bullet"></span></li>
      <li>Audio Visual<span class="bullet"></span></li>
      <li>Data Networks<span class="bullet"></span></li>
    </ul>
    <p class="reg reg--licence">Licence: #518427K</p>
    <p class="reg reg--abn">ABN: 58316927405</p>
  </section>
</body>
</html>
```